Industry automation wholesale website

www.velqora.eu provides solutions for automation, building automation and digital signage.

Our products are rugged, reliable, energy saving and representative.

Scope of pages:
● welcome page
- scope of products
- applications, success stories and news
● category page
- short introduction
- sub categories
- product highlights
● product page
- short introduction
- about 3 to 4 pictures
- technical specifications: materials, dimensions
- price
- related products

Optional:
● contact page
- address
- contact form
● blog
- picture
- text
● logo
● favicon / apple touch icon

Conclusion:
● We need a professionally looking site
● Bright colors (e.g. white, grey, metalic colors, blue)

some pages we like:
http://www.brundafel.de/
http://www.korvimash.de/

Target Market(s)

Our target market is the industrial sector
● Target audience: engineering and IT professionals

Industry/Entity Type

Building

Requirements
Must have
• ● only use free available fonts e.g. Pellor Type Library (http://www.pellortype.com/webfonts)
Should not have
• ● sound
● flash

```html
<!DOCTYPE html>
<html lang="en">
<head>
<meta charset="utf-8">
<title>Velqora – Industrial Automation</title>
<link rel="stylesheet" href="https://fonts.googleapis.com/css2?family=Ubuntu:ital,wght@0,300;0,400;0,500;1,300&display=swap">
<style>
:root{
  --brand:#1e6283;
  --brand-dark:#124c68;
  --brand-light:#2a7ea4;
  --nav-a:#1a6789;
  --nav-b:#114863;
  --search-bg:#1a2730;
  --text:#444;
  --muted:#666;
  --line:#d5d5d5;
  --white:#fff;
  --page:#fff;
}
*{box-sizing:border-box;margin:0;padding:0}
html,body{width:1200px;height:1038px;overflow:hidden;background:var(--page);font-family:'Ubuntu',sans-serif;color:var(--text)}
.canvas{position:relative;width:1200px;height:1038px;overflow:hidden}
.top-rule{position:absolute;left:0;top:0;width:1200px;height:4px;background:var(--brand)}
.bottom-rule{position:absolute;left:0;top:1028px;width:1200px;height:10px;background:var(--brand)}

.brand{position:absolute;left:126px;top:26px;color:var(--brand)}
.brand-name{font-size:54px;font-weight:400;letter-spacing:1px;line-height:56px}
.brand-tag{font-size:13px;font-weight:400;margin-top:-2px;letter-spacing:.2px}

.contact{position:absolute;top:18px;display:flex;align-items:center;gap:10px;color:var(--brand);font-size:15px;font-weight:300}
.contact.phone{left:756px}
.contact.mail{left:938px}

.language{position:absolute;left:915px;top:63px;width:163px;height:38px;border:1px solid var(--line);font-size:14px;font-style:italic;font-weight:300;color:var(--brand);padding:10px 0 0 11px}
.language svg{position:absolute;right:12px;top:15px}

.hero{position:absolute;left:0;top:151px;width:1200px;height:462px;
  background:radial-gradient(ellipse at 25% 85%,#b8e3ef 0%,rgba(120,190,215,.6) 18%,transparent 45%),
  linear-gradient(180deg,#0d2c45 0%,#1c5a78 45%,#4c9ab6 75%,#2b6a86 100%)}
.slider-dots{position:absolute;left:1001px;top:206px;display:flex;gap:9px}
.slider-dots span{width:12px;height:12px;border-radius:50%;background:#1b2a33}
.slider-dots span.active{background:var(--white)}

.nav{position:absolute;left:98px;top:128px;width:1003px;height:47px;background:linear-gradient(180deg,var(--nav-a),var(--nav-b));border:1px solid #9fb4c0;display:flex}
.nav-links{display:flex;list-style:none;padding-left:36px}
.nav-links li{color:var(--white);font-size:17px;font-weight:400;padding:13px 11px 0;margin-right:40px;position:relative}
.nav-links li.current::after{content:"";position:absolute;left:0;right:0;bottom:0;height:3px;background:var(--white)}
.nav-search{position:absolute;right:0;top:0;width:222px;height:45px;background:var(--search-bg);color:#ddd;font-size:12px;font-style:italic;font-weight:300;padding:16px 0 0 16px}
.nav-search svg{position:absolute;right:14px;top:13px}

.feature{position:absolute;left:161px;top:361px;width:481px;height:164px;background:var(--white);padding:16px 0 0 18px}
.feature h1{font-size:28px;font-weight:500;color:var(--brand);letter-spacing:.2px}
.feature ul{list-style:none;margin-top:14px}
.feature li{display:flex;font-size:16px;color:#222;height:24px;align-items:center}
.feature li svg{margin:0 8px 0 14px}
.feature .label{width:112px}

.content{position:absolute;left:110px;top:597px;width:978px;height:354px;background:var(--white);box-shadow:0 2px 10px rgba(0,0,0,.15)}
.content h2{position:absolute;top:38px;font-size:22px;font-weight:500;color:var(--brand)}
.welcome h2{left:17px}
.welcome h3{position:absolute;left:18px;top:82px;font-size:15px;font-weight:400;color:var(--brand-light)}
.welcome p{position:absolute;left:21px;top:107px;width:285px;font-size:12.5px;line-height:18px;color:var(--muted)}
.welcome p.wide{top:237px;width:270px}
.module-shot{position:absolute;left:240px;top:118px;width:100px;height:118px;border-radius:8px;background:linear-gradient(135deg,#8fa8e0,#4f6fbf 55%,#3f9a4a)}
.btn{position:absolute;background:linear-gradient(180deg,#1f6f93,#124c68);color:var(--white);border-radius:4px;font-size:13px;box-shadow:0 0 0 1px #a9c0cc}
.welcome .btn{left:20px;top:308px;width:90px;height:27px;padding:6px 0 0 12px}

.range h2{left:364px}
.range ul{position:absolute;left:368px;top:82px;list-style:none}
.range li{font-size:13px;color:var(--muted);height:30px;display:flex;align-items:center}
.range li::before{content:"";width:8px;height:8px;border-radius:50%;background:var(--brand);margin-right:16px}

.finder h2{left:633px}
.finder .field{position:absolute;left:634px;top:76px;width:285px;height:38px;border:1px solid #c8c8c8}
.finder .field svg{position:absolute;right:18px;top:9px}
.finder .btn{left:775px;top:122px;width:141px;height:28px;padding:7px 0 0 23px}
.finder .sub{top:166px;left:631px}
.showcase{position:absolute;left:631px;top:200px;width:283px;height:139px;border:1px solid #ccc;background:var(--white)}
.panel-pc{position:absolute;top:12px;height:110px;border-radius:3px}
.panel-pc.light{left:26px;width:92px;background:linear-gradient(135deg,#e4e8e8,#8aa9c9 50%,#c9cfcf)}
.panel-pc.dark{left:148px;width:108px;background:linear-gradient(135deg,#333,#5b8fc7 50%,#222)}

.footer-copy{position:absolute;left:116px;top:975px;font-size:13px;color:var(--muted);font-weight:300}
.social{position:absolute;left:893px;top:967px;display:flex;gap:10px}
.social span{width:30px;height:30px;border-radius:3px;box-shadow:0 0 0 1px rgba(0,0,0,.2)}
.social .s1{background:#3d6cb5}.social .s2{background:#35a6c8}.social .s3{background:#f08a1c}.social .s4{background:#2f6aa8}
</style>
</head>
<body>
<div class="canvas">
  <div class="top-rule"></div>

  <div class="brand">
    <div class="brand-name">velqora</div>
    <div class="brand-tag">analog digital measurements</div>
  </div>

  <div class="contact phone">
    <svg width="16" height="24" viewBox="0 0 16 24"><path d="M4 2 L8 1 L9 7 L6 8 Q6 14 9 17 L12 15 L15 20 L11 23 Q3 20 2 10 Q2 5 4 2Z" fill="#333"/></svg>
    <span>+ 49-211-5093128</span>
  </div>
  <div class="contact mail">
    <svg width="22" height="18" viewBox="0 0 22 18"><rect x="1" y="3" width="20" height="14" rx="1" fill="#dfe8ee" stroke="#7fa2b8"/><path d="M1 4 L11 11 L21 4" fill="none" stroke="#3d7aa0" stroke-width="1.5"/></svg>
    <span>info@velqora.de</span>
  </div>

  <div class="language">Select Language
    <svg width="12" height="7" viewBox="0 0 12 7"><path d="M0 0 H12 L6 7Z" fill="var(--brand)"/></svg>
  </div>

  <div class="hero" role="img" aria-label="Night skyline of illuminated office towers in blue tones">
    <div class="slider-dots"><span></span><span></span><span></span><span class="active"></span></div>
  </div>

  <nav class="nav">
    <ul class="nav-links">
      <li class="current">Home</li>
      <li>Products</li>
      <li>Contact us</li>
      <li>Shopping Cart : item(0)</li>
    </ul>
    <div class="nav-search">Search...
      <svg width="20" height="20" viewBox="0 0 20 20"><circle cx="8" cy="8" r="6" fill="none" stroke="#fff" stroke-width="2.5"/><path d="M12.5 12.5 L18 18" stroke="#fff" stroke-width="3.5" stroke-linecap="round"/></svg>
    </div>
  </nav>

  <div class="feature">
    <h1>Touch Panel PC / Bedienterminal</h1>
    <ul>
      <li><svg width="10" height="13" viewBox="0 0 10 13"><circle cx="5" cy="5" r="4" fill="none" stroke="#333" stroke-width="1.3"/><rect x="3" y="9" width="4" height="3" fill="#333"/></svg><span class="label">Industrial :</span>IP65 Front . 24/7 continuous operation</li>
      <li><svg width="10" height="13" viewBox="0 0 10 13"><circle cx="5" cy="5" r="4" fill="none" stroke="#333" stroke-width="1.3"/><rect x="3" y="9" width="4" height="3" fill="#333"/></svg><span class="label">Performance :</span>Vantor Auto DualCore1.8 GHz.</li>
      <li><svg width="10" height="13" viewBox="0 0 10 13"><circle cx="5" cy="5" r="4" fill="none" stroke="#333" stroke-width="1.3"/><rect x="3" y="9" width="4" height="3" fill="#333"/></svg><span class="label">Fanless :</span>Lowheat emission, Power Saving</li>
    </ul>
  </div>

  <main class="content">
    <section class="welcome">
      <h2>Welcome to Velqora</h2>
      <h3>Modbus RTU / RS485 Remote IO Modules</h3>
      <p>RS485 Remote IO modules are ideal<br>to realize decentralized distributed<br>IO units over long distances. We<br>provide the whole product range<br>form Remote IO Modules with RS485<br>Bus and Modbus RTU such as<br>analogue IO Modules, digital IO</p>
      <div class="module-shot" role="img" aria-label="Blue DIN rail remote IO module with green terminal blocks"></div>
      <p class="wide">Modules, Relay Modules and Timer / Counter<br>Modules. Also we provide RS422 and RS485<br>converter to RS232, USB, TCP/IP.</p>
      <div class="btn">Read more</div>
    </section>

    <section class="range">
      <h2>Range of products</h2>
      <ul>
        <li>RS422 / RS485 Converter</li>
        <li>RS422 / RS485 Repeater</li>
        <li>RS485 Remote IO</li>
        <li>RS485 Modbus IO</li>
        <li>Embedded Systems</li>
        <li>PCI-Series</li>
        <li>Industry PC</li>
        <li>Industrial Display</li>
        <li>Din Rail Power Supply</li>
      </ul>
    </section>

    <section class="finder">
      <h2>Product search</h2>
      <div class="field"><svg width="20" height="20" viewBox="0 0 20 20"><circle cx="8" cy="8" r="6" fill="none" stroke="#555" stroke-width="2"/><path d="M12.5 12.5 L18 18" stroke="#555" stroke-width="3" stroke-linecap="round"/></svg></div>
      <div class="btn">Advanced Search</div>
      <h2 class="sub">Our Products</h2>
      <div class="showcase">
        <div class="panel-pc light" role="img" aria-label="Silver framed industrial touch panel PC"></div>
        <div class="panel-pc dark" role="img" aria-label="Black framed industrial touch panel PC"></div>
      </div>
    </section>
  </main>

  <div class="footer-copy">© 2014. www.velqora.eu</div>
  <div class="social" aria-label="Social links"><span class="s1"></span><span class="s2"></span><span class="s3"></span><span class="s4"></span></div>

  <div class="bottom-rule"></div>
</div>
</body>
</html>
```